Startup Biz for Seniors needs your help!

Our business is a Startup that Employs Caregivers to do IN HOME Care of the Elderly. Our website is not yet running. But, a business similar to ours is Tallbrookcare.com

We are looking for a card that only has 4 Elements:
-Logo
- Website
- Tag Line
- Phone
We would like to see some eye catching backgrounds.
We would like to see some designs with and some without a Photo.
Would like the Photo to be of a Caregiver taking care of a Senior. The photo should show both of them smiling.

Target Market(s)

Age 35-55 who has Parents that are Elderly and need care

Industry/Entity Type

Home Health Care

Contact Information for Business Card

Want it to Pop Out to the viewer . Thinking maybe:
Side 1: LOGO with Website & Tag line
Side 2: Phone Number

Font styles to use
Other font styles liked:
• Same Font as our Logo

Colors

Designer to choose colors to be used in the design.

Requirements
Must have
• Logo, website, Tag Line, Phone number and Email: "info@velvetdays.example"
• Please use one of the photos that I have attached.
Nice to have
• Would like to see a Photo worked in that has a Care Taker taking care of an Elderly Person and they are both smiling.

```html
<!DOCTYPE html>
<html lang="en">
<head>
<meta charset="utf-8">
<title>VelvetDays.example – Business Card</title>
<link href="https://fonts.googleapis.com/css2?family=Baloo+2:wght@800&family=Courgette&family=Roboto+Condensed:wght@400&display=swap" rel="stylesheet">
<style>
  :root {
    --brand-blue: #1557a8;
    --brand-orange: #ec7a1c;
    --ink-grey: #6f6f6f;
    --card-white: #ffffff;
    --page-bg: #ece8e2;
    --photo-light: #dfe6ea;
    --photo-teal: #2bb3bf;
  }
  * { margin: 0; padding: 0; box-sizing: border-box; }
  html, body {
    width: 1200px; height: 866px; overflow: hidden;
    background: var(--page-bg);
  }
  .canvas {
    width: 1200px; height: 866px;
    display: flex; align-items: center; justify-content: center; gap: 40px;
  }
  .card {
    width: 560px; height: 320px;
    background: var(--card-white);
    border-radius: 4px;
    box-shadow: 0 6px 18px rgba(0,0,0,.18);
    position: relative; overflow: hidden;
  }
  /* Front side */
  .card-front {
    display: flex; flex-direction: column; align-items: center; justify-content: center;
  }
  .wordmark {
    font-family: "Baloo 2", sans-serif; font-weight: 800;
    font-size: 52px; line-height: 1; color: var(--brand-blue);
    letter-spacing: .5px;
  }
  .tagline {
    font-family: "Courgette", cursive;
    font-size: 26px; color: var(--brand-blue);
    margin-top: 4px; margin-left: 60px;
  }
  .phone {
    display: flex; align-items: center; gap: 12px;
    margin-top: 34px;
    font-family: "Roboto Condensed", sans-serif;
    font-size: 38px; color: var(--ink-grey);
  }
  .phone svg { width: 26px; height: 34px; }
  /* Back side */
  .card-back .photo {
    position: absolute; inset: 0;
    background: linear-gradient(120deg, var(--photo-light) 0%, #eef1f3 35%, var(--photo-teal) 70%, #8fcad0 100%);
  }
  .card-back .mark-circle {
    position: absolute; width: 290px; height: 290px; border-radius: 50%;
    right: -70px; top: -80px;
    background: var(--brand-orange);
  }
  .card-back .name-band {
    position: absolute; left: 150px; bottom: 22px;
    background: var(--card-white);
    border-radius: 40px 40px 40px 40px;
    padding: 8px 34px 4px;
    transform: rotate(-8deg);
    box-shadow: 0 2px 6px rgba(0,0,0,.12);
  }
  .name-band .wordmark { font-size: 34px; }
</style>
</head>
<body>
<main class="canvas">
  <section class="card card-front">
    <div class="wordmark">VelvetDays.example</div>
    <div class="tagline">Senior Care - Family Style</div>
    <div class="phone">
      <svg viewBox="0 0 26 34" aria-hidden="true">
        <path d="M9 2 C3 4 1 10 2 17 C3 24 7 30 12 32 L15 26 L11 23 C9 20 8 15 9 12 L13 10 L12 3 Z" fill="var(--brand-orange)"/>
      </svg>
      <span>(555) 014-2270</span>
    </div>
  </section>

  <section class="card card-back">
    <div class="photo" role="img" aria-label="Photo of a smiling caregiver in teal scrubs helping a smiling senior woman"></div>
    <div class="mark-circle" aria-hidden="true"></div>
    <div class="name-band"><div class="wordmark">VelvetDays.example</div></div>
  </section>
</main>
</body>
</html>
```